Business Card and Stationary for Scuba Dive Company and UW Photography
Deep Reef Co
Modern
Capt. Dan Hollis
CEO
4810 Harbor Ct
Marlow Key FL 34512
capt.dan@deeprfco.com
www.deeprfco.com
Master Captain, QDTA IDC Staff Instructor
Would also like another card for:
Greta Wenslow
greta@deeprfco.com
Company is focused on Scuba Diving Trips, Travel and Underwater Photography. Will be selling our photos and canvas. Will focus on dive charters and trips specializing in underwater photography.

```html
<!DOCTYPE html>
<html lang="en">
<head>
<meta charset="utf-8">
<title>Deep Reef Co — Business Card</title>
<link rel="stylesheet" href="https://fonts.googleapis.com/css2?family=Jost:wght@400;500;700&display=swap">
<style>
  :root {
    --page: #ffffff;
    --ocean-deep: #0a2a6b;
    --ocean-mid: #1456b8;
    --ocean-light: #5fb4ee;
    --card-black: #0b0b0b;
    --ink-light: #ffffff;
    --ink-soft: #d9d9d9;
    --rule: #9a9a9a;
    --accent: #4fb3e8;
  }
  * { margin: 0; padding: 0; box-sizing: border-box; }
  html, body {
    width: 1200px; height: 905px; overflow: hidden;
    background: var(--page);
    font-family: "Jost", "Futura", sans-serif;
  }
  .canvas { position: relative; width: 1200px; height: 905px; }

  .card { position: absolute; overflow: hidden; }

  /* Front card */
  .card-front {
    left: 0; top: 0; width: 817px; height: 427px;
    background:
      radial-gradient(ellipse 60% 75% at 48% 0%, rgba(170,225,255,0.55), rgba(95,180,238,0) 70%),
      linear-gradient(180deg, var(--ocean-mid) 0%, var(--ocean-deep) 100%);
  }
  .card-front .brand {
    position: absolute; left: 100px; top: 130px;
    display: flex; align-items: center; gap: 22px;
  }
  .brand-dot {
    width: 44px; height: 44px; border-radius: 50%;
    background: var(--ink-light);
  }
  .card-front .brand-name {
    font-size: 66px; font-weight: 500; color: var(--ink-light);
    letter-spacing: 1px; line-height: 1;
  }
  .card-front .web {
    position: absolute; right: 142px; top: 285px;
    font-size: 19px; color: var(--ink-light);
  }
  .card-front .about {
    position: absolute; left: 64px; top: 350px;
    font-size: 16.5px; line-height: 23px; color: var(--ink-light);
  }

  /* Back card */
  .card-back {
    left: 459px; top: 488px; width: 741px; height: 417px;
    background: var(--card-black);
  }
  .card-back .brand {
    position: absolute; left: 140px; top: 92px;
    display: flex; align-items: center; gap: 18px;
  }
  .card-back .brand-dot { width: 38px; height: 38px; background: var(--accent); }
  .card-back .brand-name {
    font-size: 56px; font-weight: 500; color: var(--accent);
    letter-spacing: 1px; line-height: 1;
  }
  .card-back .rule {
    position: absolute; left: 107px; top: 189px;
    width: 537px; height: 2px; background: var(--rule);
  }
  .contact-person {
    position: absolute; left: 107px; top: 215px;
    font-size: 21px; line-height: 28px; color: var(--ink-soft);
  }
  .contact-person .name { font-weight: 700; color: var(--ink-light); }
  .contact-details {
    position: absolute; right: 97px; top: 215px; text-align: right;
    font-size: 21px; line-height: 31px; color: var(--ink-soft);
  }
</style>
</head>
<body>
<div class="canvas">
  <section class="card card-front">
    <div class="brand">
      <span class="brand-dot"></span>
      <span class="brand-name">Deep Reef Co</span>
    </div>
    <p class="web">www.deeprfco.com</p>
    <p class="about">
      Company is focused on Scuba Diving Trips<br>
      Travel and Underwater Photography. Will be selling our photos and canvas.<br>
      Will focus on dive charters and trips specializing in underwater photography
    </p>
  </section>

  <section class="card card-back">
    <div class="brand">
      <span class="brand-dot"></span>
      <span class="brand-name">Deep Reef Co</span>
    </div>
    <div class="rule"></div>
    <div class="contact-person">
      <p class="name">Capt. Dan Hollis</p>
      <p>Master Captain, CEO</p>
      <p>QDTA IDC Staff Instructor</p>
    </div>
    <div class="contact-details">
      <p>4810 Harbor Ct</p>
      <p>Marlow Key FL 34512</p>
      <p>Cell - 555-010-0143</p>
      <p>capt.dan@deeprfco.com</p>
    </div>
  </section>
</div>
</body>
</html>
```